International Education App needs UI Design

My current app is being upgraded and totally rebranded. This app is aimed to become No1. communication app for schools worldwide. Aimed at parents and high school students it will have events, assessments, messages, newsletters, notes, policies, contact us plus much more.
It will need to be much engaging and professional than all other apps on the market. You can see them attached to compare as well as the app logo to tie in the design. You can also see my current app and why needs an upgrade.
There will need to be design for each screen.
Needs a slick and professional finish with Tranvelo Blue as the base colour.
The app is called ClassNook
You will also find a file attached which shows functionality which will help design screens.

Target Market(s)

Parents, High Schools Students

Industry/Entity Type

Education

Font styles to use
Sans Serif

Colors
0355a3

Requirements
Must have
• Sleek, modern, professional and better than examples provided.
• I need a splash screen, home screen and each of the other screens designed.

```html
<!DOCTYPE html>
<html lang="en">
<head>
<meta charset="utf-8">
<title>ClassNook – Splash</title>
<link rel="stylesheet" href="https://fonts.googleapis.com/css2?family=Open+Sans:wght@400;600;700&display=swap">
<style>
  :root {
    --bg-navy: #222c3d;
    --bg-navy-deep: #1b2433;
    --pattern-tone: #2a3548;
    --brand-blue: #3b6fc0;
    --brand-blue-light: #4c82d4;
    --tagline: #2f3b50;
    --button-fill: #243047;
    --button-border: #4a5a78;
    --white: #ffffff;
    --shadow: rgba(8, 12, 20, 0.55);
  }
  * { box-sizing: border-box; margin: 0; padding: 0; }
  html, body {
    width: 677px;
    height: 1200px;
    overflow: hidden;
    background: var(--bg-navy);
    font-family: "Open Sans", Arial, sans-serif;
  }
  .splash {
    position: relative;
    width: 677px;
    height: 1200px;
    overflow: hidden;
  }
  .splash__backdrop {
    position: absolute;
    inset: 0;
    background:
      radial-gradient(ellipse at 50% 45%, var(--pattern-tone) 0%, var(--bg-navy) 55%, var(--bg-navy-deep) 100%);
  }
  .brand {
    position: absolute;
    left: 0;
    right: 0;
    top: 474px;
    display: flex;
    flex-direction: column;
    align-items: center;
  }
  .brand__tile {
    width: 166px;
    height: 166px;
    border-radius: 28px;
    background: linear-gradient(180deg, var(--brand-blue-light) 0%, var(--brand-blue) 100%);
  }
  .brand__shadow {
    width: 230px;
    height: 22px;
    margin-top: -6px;
    border-radius: 50%;
    background: radial-gradient(ellipse at center, var(--shadow) 0%, rgba(8,12,20,0) 70%);
  }
  .brand__name {
    margin-top: 2px;
    font-size: 78px;
    font-weight: 600;
    letter-spacing: 0.5px;
    line-height: 1;
    color: var(--brand-blue);
  }
  .brand__tagline {
    margin-top: 14px;
    font-size: 34px;
    font-weight: 400;
    color: var(--tagline);
    line-height: 1;
  }
  .actions {
    position: absolute;
    top: 1047px;
    left: 79px;
    right: 79px;
    display: flex;
    justify-content: space-between;
  }
  .action-button {
    display: flex;
    align-items: center;
    justify-content: center;
    gap: 14px;
    width: 188px;
    height: 52px;
    border-radius: 26px;
    background: var(--button-fill);
    border: 2px solid var(--button-border);
    color: var(--white);
    font-size: 18px;
    font-weight: 700;
    letter-spacing: 0.5px;
    text-transform: uppercase;
  }
  .action-button svg { width: 22px; height: 22px; fill: var(--white); }
</style>
</head>
<body>
  <main class="splash">
    <div class="splash__backdrop" role="img" aria-label="Faint hand-drawn school doodles on a dark navy background"></div>

    <section class="brand">
      <div class="brand__tile"></div>
      <div class="brand__shadow"></div>
      <h1 class="brand__name">ClassNook</h1>
      <p class="brand__tagline">education</p>
    </section>

    <nav class="actions">
      <div class="action-button action-button--call">
        <svg viewBox="0 0 24 24" aria-hidden="true"><path d="M6.6 10.8a15.2 15.2 0 0 0 6.6 6.6l2.2-2.2c.3-.3.7-.4 1-.2 1.1.4 2.3.6 3.6.6.6 0 1 .4 1 1V20c0 .6-.4 1-1 1A17 17 0 0 1 3 4c0-.6.4-1 1-1h3.5c.6 0 1 .4 1 1 0 1.3.2 2.5.6 3.6.1.3 0 .7-.2 1z"/></svg>
        <span>Call us</span>
      </div>
      <div class="action-button action-button--share">
        <svg viewBox="0 0 24 24" aria-hidden="true"><path d="M18 16.1c-.8 0-1.5.3-2 .8l-7.1-4.2c.1-.2.1-.5.1-.7s0-.5-.1-.7L16 7.2c.5.5 1.2.8 2 .8a3 3 0 1 0-3-3c0 .2 0 .5.1.7L8 9.8A3 3 0 1 0 8 14.2l7.1 4.2c-.1.2-.1.4-.1.6a2.9 2.9 0 1 0 3-2.9z"/></svg>
        <span>Share</span>
      </div>
    </nav>
  </main>
</body>
</html>
```